KA VERLINE

We need a letterhead design for an Image & Etiquette Consultancy company based in Singapore.

The services we provide are Personal Image Consultation, Image & Etiquette Workshop for schools and corporate.

The design should have our corporate colour as seen in the logo files I have uploaded.

Since our company helps clients with their image, the design should be aesthetically very appealing. It should reflect a very classy & elegant feel.

I will print the letterhead using my printer but most of the time will use it to write letters to my clients therefore the format should include MS Word.

```html
<!DOCTYPE html>
<html lang="en">
<head>
<meta charset="UTF-8">
<title>Ka Verline Letterhead</title>
<link rel="stylesheet" href="https://fonts.googleapis.com/css2?family=Questrial&family=Open+Sans:wght@400;600&family=Michroma&display=swap">
<style>
  :root {
    --plum: #2e1a47;
    --gold: #c9a227;
    --gold-light: #f3e49a;
    --ink: #3a3a3a;
    --paper: #ffffff;
    --backdrop: #e2e2e0;
  }
  * { margin: 0; padding: 0; box-sizing: border-box; }
  html, body {
    width: 1200px; height: 1200px; overflow: hidden;
    background: var(--backdrop);
  }
  .letterhead {
    position: absolute; left: 273px; top: 138px;
    width: 653px; height: 922px;
    background: var(--paper);
  }
  .top-band {
    position: absolute; left: 0; top: 0; width: 100%; height: 12px;
    background: var(--plum);
  }
  .brand-name {
    position: absolute; left: 33px; top: 52px;
    font-family: "Questrial", sans-serif;
    font-size: 33px; letter-spacing: 1px;
    color: var(--plum);
  }
  .footer-company {
    position: absolute; left: 33px; top: 840px;
    font-family: "Michroma", sans-serif;
    font-size: 13px; font-weight: 400;
    color: var(--plum);
  }
  .footer-text {
    font-family: "Open Sans", sans-serif;
    font-size: 10px; line-height: 15px;
    color: var(--ink);
  }
  .footer-address { position: absolute; left: 33px; top: 865px; }
  .contact-list { position: absolute; top: 861px; list-style: none; }
  .contact-list li { display: flex; align-items: center; gap: 6px; height: 16px; }
  .contact-list svg { width: 10px; height: 10px; fill: var(--plum); }
  .contact-phone { left: 243px; }
  .contact-online { left: 377px; }
  .bottom-band {
    position: absolute; left: 0; bottom: 0; width: 653px; height: 12px;
  }
</style>
</head>
<body>
  <main class="letterhead">
    <div class="top-band"></div>

    <div class="brand-name">KA VERLINE</div>

    <footer>
      <div class="footer-company">Ka Verline Limited</div>
      <div class="footer-address footer-text">
        Your Long address with code no.<br>
        your licence no.: xxx xxx xxx xx
      </div>

      <ul class="contact-list contact-phone footer-text">
        <li>
          <svg viewBox="0 0 10 10"><path d="M1 3 Q5 0 9 3 L8 4.5 L6.5 3.8 L6.5 3 Q5 2.5 3.5 3 L3.5 3.8 L2 4.5 Z M2.5 5 H7.5 L8.5 9 H1.5 Z"/></svg>
          000 000 000 000
        </li>
        <li>
          <svg viewBox="0 0 10 10"><path d="M1 3 Q5 0 9 3 L8 4.5 L6.5 3.8 L6.5 3 Q5 2.5 3.5 3 L3.5 3.8 L2 4.5 Z M2.5 5 H7.5 L8.5 9 H1.5 Z"/></svg>
          123 456 789&nbsp; 123
        </li>
      </ul>

      <ul class="contact-list contact-online footer-text">
        <li>
          <svg viewBox="0 0 10 10"><path d="M0.5 2 H9.5 V8 H0.5 Z M0.5 2 L5 5.5 L9.5 2" fill="var(--plum)" stroke="#fff" stroke-width="0.6"/></svg>
          yourname@kaverline.com
        </li>
        <li>
          <svg viewBox="0 0 10 10"><circle cx="5" cy="5" r="4.5"/><path d="M0.5 5 H9.5 M5 0.5 V9.5 M5 0.5 Q2 5 5 9.5 M5 0.5 Q8 5 5 9.5" stroke="#fff" stroke-width="0.6" fill="none"/></svg>
          www.kaverline.com
        </li>
      </ul>

      <svg class="bottom-band" viewBox="0 0 653 12" preserveAspectRatio="none">
        <defs>
          <linearGradient id="goldSheen" x1="0" x2="1" y1="0" y2="0">
            <stop offset="0" stop-color="#b8860b"/>
            <stop offset="0.25" stop-color="#e8c21a"/>
            <stop offset="0.5" stop-color="#f6eda0"/>
            <stop offset="0.75" stop-color="#e5b80f"/>
            <stop offset="1" stop-color="#b8902e"/>
          </linearGradient>
        </defs>
        <rect x="0" y="0" width="653" height="12" fill="var(--plum)"/>
        <polygon points="420,0 653,0 653,12 390,12" fill="url(#goldSheen)"/>
      </svg>
    </footer>
  </main>
</body>
</html>
```